High end boutique food product label

We are looking for a label design to be used on our range of high end food products. We don't have a design or colour scheme in mind and are interested to see what ideas are submitted.
We would like it to feel sophisticated, chic, and eye-catching.
All of our products are handmade in Australia using Australian ingredients.
The graphics for the label will need to be scaleable to be fit a variety of labels from small squat jars with labels sized 3.5cm high and 7cm wide, to tall thin bottles with labels that are 14cm high and 4.5cm wide.
We would be interested in working with the winning designer to create these different sized labels.
The label submitted for this project should be 14cm high and 4.5cm wide, it should include our logo (file supplied in .jpeg and .ai), the product name 'Extra Virgin Olive Oil' and the size '250ml'.
This is just the front label on a bottle, we are not expecting a rear label to be created currently.
You are welcome to use any fonts you think will look good but the fonts used in our logo are Allaina Medium and Bebas Kai Regular.

```html
<!DOCTYPE html>
<html lang="en">
<head>
<meta charset="utf-8">
<title>Hale &amp; Finch – Extra Virgin Olive Oil Labels</title>
<link rel="stylesheet" href="https://fonts.googleapis.com/css2?family=Abril+Fatface&display=swap">
<style>
  :root {
    --brown: #3d2a1e;
    --tan: #b9a986;
    --white: #ffffff;
    --brown-leaf: #5a4433;
    --tan-leaf: #cbbd9e;
    --white-leaf: #efebe3;
    --frame: #2a2a2a;
  }
  * { margin: 0; padding: 0; box-sizing: border-box; }
  html, body {
    width: 1200px;
    height: 906px;
    overflow: hidden;
    background: var(--white);
  }
  .sheet {
    position: relative;
    width: 1200px;
    height: 906px;
  }
  .label {
    position: absolute;
    top: 53px;
    width: 252px;
    height: 782px;
    overflow: hidden;
    font-family: "Abril Fatface", serif;
    text-align: center;
  }
  .label--dark  { left: 84px;  background: var(--brown); }
  .label--tan   { left: 473px; background: var(--tan); }
  .label--light { left: 861px; background: var(--white); border: 1px solid var(--frame); }

  .label__branch {
    position: absolute;
    inset: 0;
  }
  .label--dark .label__branch {
    background: radial-gradient(ellipse 60% 75% at 62% 55%, var(--brown-leaf) 0%, rgba(90,68,51,0) 70%);
    opacity: .6;
  }
  .label--tan .label__branch {
    background: radial-gradient(ellipse 60% 75% at 62% 55%, var(--tan-leaf) 0%, rgba(203,189,158,0) 70%);
    opacity: .7;
  }
  .label--light .label__branch {
    background: radial-gradient(ellipse 60% 75% at 62% 55%, var(--white-leaf) 0%, rgba(239,235,227,0) 70%);
  }

  .brand {
    position: absolute;
    top: 136px;
    left: 0;
    right: 0;
    font-size: 30px;
    line-height: 1;
    letter-spacing: .5px;
  }
  .label--dark .brand, .label--tan .brand { color: var(--white); }
  .label--light .brand { color: var(--brown); }

  .product {
    position: absolute;
    top: 327px;
    left: -10px;
    right: -10px;
    font-size: 66px;
    line-height: 62px;
    font-weight: 400;
  }
  .product span { display: block; }

  .label--dark .product__lead  { color: var(--white); }
  .label--dark .product__tail  { color: var(--tan); }
  .label--tan .product__lead   { color: var(--white); }
  .label--tan .product__tail   { color: var(--brown); }
  .label--light .product__lead { color: var(--brown); }
  .label--light .product__tail { color: var(--tan); }

  .volume {
    position: absolute;
    top: 717px;
    left: 0;
    right: 0;
    font-size: 23px;
    line-height: 1;
  }
  .label--dark .volume, .label--tan .volume { color: var(--white); }
  .label--light .volume { color: var(--brown); }
</style>
</head>
<body>
<main class="sheet">
  <section class="label label--dark">
    <div class="label__branch" role="img" aria-label="Faint olive branch illustration in a slightly lighter brown"></div>
    <p class="brand">Hale &amp; Finch</p>
    <h1 class="product">
      <span class="product__lead">Extra</span>
      <span class="product__lead">Virgin</span>
      <span class="product__tail">Olive</span>
      <span class="product__tail">Oil</span>
    </h1>
    <p class="volume">250ml</p>
  </section>

  <section class="label label--tan">
    <div class="label__branch" role="img" aria-label="Faint olive branch illustration in a lighter tan"></div>
    <p class="brand">Hale &amp; Finch</p>
    <h1 class="product">
      <span class="product__lead">Extra</span>
      <span class="product__lead">Virgin</span>
      <span class="product__tail">Olive</span>
      <span class="product__tail">Oil</span>
    </h1>
    <p class="volume">250ml</p>
  </section>

  <section class="label label--light">
    <div class="label__branch" role="img" aria-label="Faint olive branch illustration in pale cream"></div>
    <p class="brand">Hale &amp; Finch</p>
    <h1 class="product">
      <span class="product__lead">Extra</span>
      <span class="product__lead">Virgin</span>
      <span class="product__tail">Olive</span>
      <span class="product__tail">Oil</span>
    </h1>
    <p class="volume">250ml</p>
  </section>
</main>
</body>
</html>
```